Business Card Design Project

My business sells promotional merchandise to large blue chip companies. Gear like polo shirts, drink bottles, pens, basically anything that you can put a company logo onto.

I need the following elements included:
Logo as attached
Peter Hollingdale Managing Director
27 Corbel Street Tarrin Cove 4178
mobile 0438 514203
email kestrelpath@kestrelpathtrading.com.au

Promotional Merchandise with a difference

Target Market(s)

Mature age Marketing Managers

Industry/Entity Type

Business

```html
<!DOCTYPE html>
<html lang="en">
<head>
<meta charset="utf-8">
<title>Kestrelpath Business Card</title>
<link rel="stylesheet" href="https://fonts.googleapis.com/css2?family=Open+Sans:wght@400;600;700&display=swap">
<style>
  :root {
    --navy: #0b2d62;
    --white: #ffffff;
    --ink: #4a4a4a;
    --text: #222222;
    --rule: #777777;
    --card-edge: #d4d4d4;
    --page: #ffffff;
  }
  * { box-sizing: border-box; margin: 0; padding: 0; }
  html, body {
    width: 1200px;
    height: 900px;
    overflow: hidden;
    background: var(--page);
    font-family: "Open Sans", Arial, sans-serif;
  }
  .canvas {
    position: relative;
    width: 1200px;
    height: 900px;
  }
  .card {
    position: absolute;
    top: 290px;
    width: 524px;
    height: 320px;
    border-radius: 8px;
    overflow: hidden;
  }
  .card--front {
    left: 62px;
    background: var(--white);
    border: 1px solid var(--card-edge);
  }
  .card--back {
    left: 612px;
    background: var(--navy);
  }
  .front-header {
    height: 124px;
    background: var(--navy);
    display: flex;
    align-items: center;
    justify-content: center;
  }
  .brand-name {
    font-family: "Open Sans", Arial, sans-serif;
    font-weight: 600;
    letter-spacing: 1px;
    line-height: 1;
  }
  .front-header .brand-name {
    color: var(--white);
    font-size: 50px;
  }
  .contact {
    text-align: center;
    color: var(--text);
  }
  .contact__name {
    margin-top: 38px;
    font-size: 22px;
    font-weight: 700;
    color: var(--ink);
    line-height: 1.1;
  }
  .contact__role {
    margin-top: 2px;
    font-size: 15px;
    font-weight: 700;
    color: var(--ink);
  }
  .contact__rule {
    width: 244px;
    height: 1px;
    margin: 24px auto 4px;
    background: var(--rule);
  }
  .contact__line {
    font-size: 13px;
    line-height: 18px;
    display: flex;
    align-items: center;
    justify-content: center;
    gap: 6px;
  }
  .contact__line svg { display: block; }
  .back-band {
    position: absolute;
    left: 0;
    top: 126px;
    width: 100%;
    height: 70px;
    background: var(--white);
    display: flex;
    align-items: center;
    justify-content: center;
  }
  .back-band .brand-name {
    color: var(--navy);
    font-size: 38px;
  }
</style>
</head>
<body>
<main class="canvas">
  <section class="card card--front" aria-label="Business card front">
    <header class="front-header">
      <span class="brand-name">KESTRELPATH</span>
    </header>
    <div class="contact">
      <p class="contact__name">Peter Hollingdale</p>
      <p class="contact__role">Managing Director</p>
      <div class="contact__rule"></div>
      <p class="contact__line">27 Corbel Street Tarrin Cove 4178</p>
      <p class="contact__line">
        <svg width="8" height="12" viewBox="0 0 8 12" aria-hidden="true">
          <rect x="0.5" y="0.5" width="7" height="11" rx="1.2" fill="var(--text)"/>
          <rect x="1.8" y="2" width="4.4" height="6" fill="var(--white)"/>
        </svg>
        0438 514203
      </p>
      <p class="contact__line">
        <svg width="12" height="8" viewBox="0 0 12 8" aria-hidden="true">
          <rect x="0" y="0" width="12" height="8" fill="var(--text)"/>
          <path d="M0.5 0.5 L6 4.5 L11.5 0.5" fill="none" stroke="var(--white)" stroke-width="1"/>
        </svg>
        kestrelpath@kestrelpathtrading.com.au
      </p>
    </div>
  </section>

  <section class="card card--back" aria-label="Business card back">
    <div class="back-band">
      <span class="brand-name">KESTRELPATH</span>
    </div>
  </section>
</main>
</body>
</html>
```